Bref créative
Limb Nestler
Naturally made in the US
Professional
Rosalind Featherstone
Owner
437 Tamsin Ave - Ste 220-581
rfeatherstone@limbnestler-example.com
Limbnestler-example.com
I'm not sure what the first two boxes refer to. I want our logo to be on the cards in the same colors.

```html
<!DOCTYPE html>
<html lang="en">
<head>
<meta charset="utf-8">
<title>Limb Nestler – Business Card</title>
<link rel="stylesheet" href="https://fonts.googleapis.com/css2?family=Open+Sans:ital,wght@0,400;0,700;1,400&family=Questrial&display=swap">
<style>
  :root {
    --brown: #7b3b37;
    --blue: #2a9fd9;
    --white: #ffffff;
    --grey: #5a5a5a;
    --body-font: "Open Sans", Arial, sans-serif;
    --brand-font: "Questrial", "Century Gothic", sans-serif;
  }
  html, body {
    margin: 0;
    padding: 0;
    overflow: hidden;
    background: var(--white);
  }
  .card {
    position: relative;
    width: 1200px;
    height: 689px;
    overflow: hidden;
    background: var(--white);
    font-family: var(--body-font);
  }
  .band {
    position: absolute;
    left: 0;
    width: 100%;
    background: var(--brown);
  }
  .band--top { top: 0; height: 92px; border-bottom: 5px solid var(--blue); }
  .band--bottom { bottom: 0; height: 175px; border-top: 5px solid var(--blue); }

  .identity {
    position: absolute;
    top: 16px;
    right: 46px;
    text-align: right;
    color: var(--white);
  }
  .identity__name { margin: 0; font-weight: 700; font-size: 31px; line-height: 1.2; }
  .identity__role { margin: 0; font-size: 25px; line-height: 1.2; }

  .brand-mark {
    position: absolute;
    left: 490px;
    top: 110px;
    width: 220px;
    height: 220px;
  }
  .brand-name {
    position: absolute;
    left: 0;
    width: 100%;
    top: 384px;
    margin: 0;
    text-align: center;
    font-family: var(--brand-font);
    font-weight: 400;
    font-size: 74px;
    line-height: 1;
    color: var(--grey);
  }
  .tagline {
    position: absolute;
    left: 0;
    width: 100%;
    top: 466px;
    margin: 0;
    padding-right: 70px;
    box-sizing: border-box;
    text-align: center;
    font-style: italic;
    font-size: 28px;
    line-height: 1;
    color: var(--grey);
  }

  .contact {
    position: absolute;
    left: 0;
    width: 100%;
    bottom: 30px;
    margin: 0;
    text-align: center;
    color: var(--white);
    font-size: 24px;
    line-height: 38px;
  }
  .contact__web { font-weight: 700; font-size: 26px; }
  .contact__label { color: var(--blue); font-weight: 700; }
</style>
</head>
<body>
<main class="card">
  <div class="band band--top"></div>
  <div class="band band--bottom"></div>

  <header class="identity">
    <p class="identity__name">Rosalind Featherstone</p>
    <p class="identity__role">Owner</p>
  </header>

  <svg class="brand-mark" viewBox="0 0 220 220" aria-hidden="true">
    <circle cx="110" cy="110" r="110" fill="var(--blue)"/>
  </svg>
  <h1 class="brand-name">limb nestler</h1>
  <p class="tagline">naturally made in the US</p>

  <address class="contact">
    <div class="contact__web">www.Limbnestler-example.com</div>
    <div><span class="contact__label">A:</span> 437 Tamsin Ave - Ste 220-581</div>
    <div><span class="contact__label">P:</span> 877-555-0142 | <span class="contact__label">C:</span> 515-555-0178 <span class="contact__label">E:</span> rfeatherstone@limbnestler-example.com</div>
  </address>
</main>
</body>
</html>
```